Business card for Chicago based Private Equity Company

We need a business card for our PE company called Crestline Partners. We want a simple and clean, yet creative card design. The back side should reflect our logo. Also would like to see embossed ideas. Should reflect strength and growth. Our logo is attached. Also need editable file. Details are as follows for Business Card:

Dale Moravec Co-Founder 2750 Larkin Avenue Suite 410 Oak Brook, IL 60587 http://www.crestlinepartnersllc.example (D) 630.555.0142 (C) 312.555.0178 (E) dm@crestlinepartnersllc.example

```html
<!DOCTYPE html>
<html lang="en">
<head>
<meta charset="utf-8">
<title>Crestline Partners – Business Card</title>
<link href="https://fonts.googleapis.com/css2?family=Exo+2:wght@400;500;600&display=swap" rel="stylesheet">
<style>
  :root {
    --backdrop: #e8e4e0;
    --card: #ffffff;
    --card-shade: #eceef0;
    --blue: #1f8ad8;
    --blue-deep: #1567b6;
    --charcoal: #34373c;
    --ink: #2f3236;
    --ink-soft: #5a5e63;
  }
  * { margin: 0; padding: 0; box-sizing: border-box; }
  html, body {
    width: 1200px; height: 900px; overflow: hidden;
    background: var(--backdrop);
    font-family: "Exo 2", sans-serif;
    color: var(--ink);
  }
  .stage {
    width: 1200px; height: 900px;
    display: flex; align-items: center; justify-content: center; gap: 40px;
  }
  .card {
    position: relative;
    width: 540px; height: 309px;
    background: radial-gradient(ellipse at 55% 40%, var(--card) 0%, var(--card) 45%, var(--card-shade) 100%);
    box-shadow: 0 10px 24px rgba(0,0,0,.18);
    overflow: hidden;
  }
  .card__band { position: absolute; inset: 0; width: 100%; height: 100%; }

  .brand { display: flex; align-items: center; gap: 14px; }
  .brand__dot {
    width: 30px; height: 30px; border-radius: 50%;
    background: var(--blue); flex: none;
  }
  .brand__name {
    font-weight: 500; color: var(--charcoal);
    letter-spacing: 3px; text-transform: uppercase; line-height: 1.15;
  }
  .brand__line { display: block; white-space: nowrap; }

  .front .brand { position: absolute; left: 44px; top: 92px; }
  .front .brand__name { font-size: 22px; }
  .front .brand__dot { width: 38px; height: 38px; }

  .person { position: absolute; left: 310px; top: 46px; }
  .person__name { font-size: 15px; font-weight: 600; letter-spacing: 1px; text-transform: uppercase; }
  .person__title { font-size: 11px; color: var(--ink-soft); margin-top: 2px; }

  .contacts { position: absolute; left: 310px; top: 100px; list-style: none; }
  .contacts li {
    display: flex; align-items: center; gap: 8px;
    font-size: 10.5px; color: var(--ink); height: 17px; white-space: nowrap;
  }
  .contacts svg { width: 10px; height: 10px; fill: var(--charcoal); flex: none; }

  .address {
    position: absolute; left: 34px; bottom: 22px;
    font-size: 13px; color: #fff; letter-spacing: .5px;
  }

  .back { display: flex; align-items: center; justify-content: center; }
  .back .brand__name { font-size: 26px; }
  .back .brand__dot { width: 42px; height: 42px; }
</style>
</head>
<body>
<main class="stage">

  <section class="card front" aria-label="Card front">
    <svg class="card__band" viewBox="0 0 540 309" preserveAspectRatio="none" aria-hidden="true">
      <defs>
        <linearGradient id="bandShade" x1="0" y1="0" x2="1" y2="0">
          <stop offset="0" stop-color="var(--blue-deep)" stop-opacity=".6"/>
          <stop offset="1" stop-color="var(--blue)" stop-opacity="0"/>
        </linearGradient>
      </defs>
      <path d="M0 214 C 150 232, 330 262, 540 262 L540 272 C 330 272, 150 246, 0 232 Z" fill="var(--charcoal)"/>
      <path d="M0 230 C 150 244, 330 270, 540 270 L540 309 L0 309 Z" fill="var(--blue)"/>
      <path d="M0 230 C 150 244, 330 270, 540 270 L540 309 L0 309 Z" fill="url(#bandShade)"/>
    </svg>

    <div class="brand">
      <span class="brand__dot"></span>
      <span class="brand__name">
        <span class="brand__line">Crestline</span>
        <span class="brand__line">Partners</span>
      </span>
    </div>

    <div class="person">
      <p class="person__name">Dale Moravec</p>
      <p class="person__title">Managing Director</p>
    </div>

    <ul class="contacts">
      <li>
        <svg viewBox="0 0 10 10"><path d="M2 0h2l1 2.5-1.3 1a5 5 0 0 0 2.8 2.8l1-1.3L10 6v2a2 2 0 0 1-2 2A8 8 0 0 1 0 2a2 2 0 0 1 2-2z"/></svg>
        630.555.0142
      </li>
      <li>
        <svg viewBox="0 0 10 10"><path d="M2.5 0h5a1 1 0 0 1 1 1v8a1 1 0 0 1-1 1h-5a1 1 0 0 1-1-1V1a1 1 0 0 1 1-1zm.3 1.2v6.6h4.4V1.2z"/></svg>
        312.555.0178
      </li>
      <li>
        <svg viewBox="0 0 10 10"><path d="M0 2h10v6H0zM.8 2.6 5 5.6l4.2-3H.8z"/></svg>
        dm@crestlinepartnersllc.example
      </li>
      <li>
        <svg viewBox="0 0 10 10"><path d="M5 0a5 5 0 1 0 0 10A5 5 0 0 0 5 0zm0 1c.7.8 1.1 2 1.2 3.5H3.8C3.9 3 4.3 1.8 5 1zM1 5.5h1.8c.1 1.4.5 2.5 1 3.3A4 4 0 0 1 1 5.5zm0-1a4 4 0 0 1 2.8-3.3c-.5.8-.9 1.9-1 3.3zm4 4.5c-.7-.8-1.1-2-1.2-3.5h2.4C6.1 7 5.7 8.2 5 9zm1.2-.2c.5-.8.9-1.9 1-3.3H9a4 4 0 0 1-2.8 3.3zm1-4.3c-.1-1.4-.5-2.5-1-3.3A4 4 0 0 1 9 4.5z"/></svg>
        www.crestlinepartnersllc.example
      </li>
    </ul>

    <p class="address">2750 Larkin Avenue Suite 410</p>
  </section>

  <section class="card back" aria-label="Card back">
    <div class="brand">
      <span class="brand__dot"></span>
      <span class="brand__name">Crestline Partners</span>
    </div>
  </section>

</main>
</body>
</html>
```